Harvest Gathering event flyer

I would like a church event flyer designed. The event is called "HARVEST GATHERING 2018". I am looking for a professional, yet catchy design that uses our brand colors and logo creatively while communicating key information of the event effectively.

1. The logo is attached in two color formats. The designer has the choice to use them as he/she want.

2. The location of the event is: Lindqvist Community Center, 482 Tamsworth Street, Portland, ME 04102
3. Time and date of event. The designer can organize and format the date and time as he/she pleases.
December 28th, 29th @ 7:00PM
December 30th @ 10:00AM
4. The topic of the event is "Tongues of fire". The designer is free to use this phrase as he/she pleases to create a good composition.
5. Speaker: Prophet Marcus Obuya
6. Contact information: contact@cedarbrookfellowship.org - Telephone number: 207 555 0148

7. I would also like the following three words on the flyer. These words describe the focus of the event: FIRE, REVIVAL, PROPHETIC

```html
<!DOCTYPE html>
<html lang="en">
<head>
<meta charset="utf-8">
<title>Harvest Gathering 2018</title>
<link href="https://fonts.googleapis.com/css2?family=Poppins:wght@800&family=League+Spartan:wght@800&family=Great+Vibes&display=swap" rel="stylesheet">
<style>
  :root {
    --navy: #0b1226;
    --navy-deep: #05080f;
    --gold-light: #ffd84a;
    --gold: #f2a81f;
    --orange: #e0681c;
    --red: #c8182a;
    --cream: #e6dfc7;
    --white: #ffffff;
  }
  * { margin: 0; padding: 0; box-sizing: border-box; }
  html, body { width: 849px; height: 1200px; overflow: hidden; background: var(--navy-deep); }
  .flyer {
    position: relative; width: 849px; height: 1200px; overflow: hidden;
    font-family: "League Spartan", "Poppins", sans-serif; font-weight: 800;
  }
  .backdrop {
    position: absolute; inset: 0;
    background:
      radial-gradient(circle at 55% 40%, rgba(120,110,80,.35), transparent 45%),
      radial-gradient(circle at 80% 75%, rgba(90,100,110,.3), transparent 40%),
      radial-gradient(circle at 20% 60%, rgba(70,60,40,.3), transparent 40%),
      linear-gradient(180deg, var(--navy) 0%, #121a2c 50%, var(--navy-deep) 100%);
  }
  .gold {
    background: linear-gradient(180deg, var(--gold-light) 0%, var(--gold) 50%, var(--orange) 100%);
    -webkit-background-clip: text; background-clip: text; color: transparent;
  }
  .title-block {
    position: absolute; left: 0; top: 22px; width: 849px; text-align: center;
    font-family: "Poppins", sans-serif; font-weight: 800; font-size: 150px;
    letter-spacing: -4px; line-height: 1;
  }
  .title-script {
    position: absolute; left: 40px; top: 140px; width: 780px; text-align: center;
    font-family: "Great Vibes", cursive; font-weight: 400; font-size: 170px; line-height: 1;
    transform: rotate(-4deg);
  }
  .year {
    position: absolute; left: 236px; top: 352px;
    font-size: 92px; line-height: 1; letter-spacing: -1px;
  }
  .emblem {
    position: absolute; left: 484px; top: 276px; width: 360px; height: 360px;
    border-radius: 50%; background: var(--cream);
    border: 5px solid var(--gold);
    display: flex; align-items: center; justify-content: center;
  }
  .emblem-name { font-size: 56px; line-height: 1; color: var(--orange); }
  .schedule { position: absolute; left: 58px; top: 480px; color: var(--cream); }
  .schedule p { font-size: 36px; line-height: 38px; letter-spacing: -1px; white-space: nowrap; }
  .schedule .gap { margin-top: 8px; }
  .location {
    position: absolute; left: 58px; top: 652px; color: var(--cream);
    font-size: 14.5px; white-space: nowrap;
  }
  .topic {
    position: absolute; left: 60px; top: 690px; width: 760px;
    font-family: "Great Vibes", cursive; font-weight: 400; font-size: 132px; line-height: 1.1;
    z-index: 2; white-space: nowrap;
  }
  .speaker-band {
    position: absolute; left: 0; top: 828px; width: 849px; height: 184px;
    background: linear-gradient(180deg, var(--gold) 0%, var(--orange) 40%, var(--red) 100%);
    text-align: center; color: var(--cream);
  }
  .speaker-label { font-size: 62px; line-height: 1; padding-top: 44px; }
  .speaker-name { font-size: 62px; line-height: 1; margin-top: 8px; white-space: nowrap; letter-spacing: -1px; }
  .focus {
    position: absolute; left: 0; top: 1030px; width: 849px; text-align: center;
    font-size: 46px; line-height: 1; white-space: nowrap;
  }
  .contact {
    position: absolute; left: 0; top: 1096px; width: 849px; text-align: center;
    color: var(--white); font-size: 22px; line-height: 32px;
  }
  .contact .details { font-size: 19px; white-space: nowrap; }
</style>
</head>
<body>
<main class="flyer">
  <div class="backdrop" role="img" aria-label="Dark navy background with soft out-of-focus golden bokeh lights"></div>

  <h1 class="title-block gold">HARVEST</h1>
  <div class="title-script gold">Gathering</div>
  <div class="year gold">2018</div>

  <div class="emblem">
    <span class="emblem-name">HALVERN</span>
  </div>

  <section class="schedule">
    <p>DECEMBER 28TH, 29TH</p>
    <p>7:00PM</p>
    <p class="gap">DECEMBER 30TH</p>
    <p>10:00AM</p>
  </section>
  <p class="location">LOCATION : LINDQVIST COMMUNITY CENTER, 482 TAMSWORTH STREET, PORTLAND, ME 04102</p>

  <h2 class="topic gold">Tongues of fire</h2>

  <section class="speaker-band">
    <p class="speaker-label">SPEAKER:</p>
    <p class="speaker-name">PROPHET MARCUS OBUYA</p>
  </section>

  <p class="focus gold">FIRE, REVIVAL, PROPHETIC</p>

  <section class="contact">
    <p>CONTACT INFORMATION:</p>
    <p class="details">CONTACT@CEDARBROOKFELLOWSHIP.ORG – TELEPHONE NUMBER: 207 555 0148</p>
  </section>
</main>
</body>
</html>
```